Modern Website Template

We need a set of modern website templates and would like to see what you can come up with.

The template should be easily customizable by an end user so they can easily swap out generic images with their own image if needed.

Some examples of templates you can create would be;
Small Business
Lawyer
Teacher
Birthday Party
Real Estate Agent
Doctor
Travel
Sports
Wedding
Religious

If we like your work we will be looking for more templates to be created.

**TEMPLATE MUST BE ORIGINAL AND NOT RESOLD**

Industry/Entity Type

Business

```html
<!DOCTYPE html>
<html lang="en">
<head>
<meta charset="utf-8">
<title>John Doe weds Alexa – Wedding Album</title>
<link rel="stylesheet" href="https://fonts.googleapis.com/css2?family=Noto+Sans:wght@400;700&family=Great+Vibes&family=Arimo&display=swap">
<style>
  :root {
    --gold: #e0a81c;
    --gold-dark: #c98e0c;
    --gold-pale: #f3e3a4;
    --cream: #fbf4dc;
    --red: #b5121b;
    --text: #333333;
    --muted: #777777;
    --icon-grey: #b8b8b8;
    --white: #ffffff;
  }
  * { box-sizing: border-box; margin: 0; padding: 0; }
  html, body { width: 1200px; height: 960px; overflow: hidden; background: var(--white); }
  body { position: relative; font-family: "Noto Sans", sans-serif; color: var(--text); }

  .site-header {
    position: absolute; left: 0; top: 0; width: 1200px; height: 150px;
    background: linear-gradient(to bottom, var(--gold-pale) 0%, var(--cream) 55%, var(--white) 100%);
  }
  .rule { position: absolute; left: 216px; width: 768px; height: 1px; background: var(--gold); }
  .rule-top { top: 94px; }
  .rule-bottom { top: 127px; }
  .event-date, .event-venue {
    position: absolute; top: 57px; font-size: 12.5px; color: var(--red);
  }
  .event-date { left: 261px; }
  .event-venue { left: 804px; }

  .main-nav { position: absolute; left: 234px; top: 103px; font-size: 10.5px; }
  .main-nav a { color: var(--text); text-decoration: none; }
  .main-nav .sep { margin: 0 6px; }

  .album-actions { position: absolute; left: 756px; top: 103px; display: flex; gap: 22px; font-size: 10.5px; color: var(--text); }
  .album-actions span { display: flex; align-items: center; gap: 6px; }

  .couple-crest { position: absolute; left: 452px; top: 4px; width: 296px; height: 142px; }
  .couple-names { position: absolute; left: 452px; top: 4px; width: 296px; height: 142px; color: var(--red); text-align: center; }
  .couple-names span { position: absolute; left: 0; width: 100%; display: block; }
  .couple-names .groom { top: 20px; font-family: "Great Vibes", cursive; font-size: 40px; line-height: 44px; }
  .couple-names .weds { top: 64px; font-size: 12px; line-height: 14px; color: var(--muted); }
  .couple-names .bride { top: 80px; font-family: "Great Vibes", cursive; font-size: 42px; line-height: 46px; }

  .photo-grid { position: absolute; left: 0; top: 0; }
  .photo-card { position: absolute; width: 138px; }
  .photo-card .frame { border-top: 1px solid var(--red); border-bottom: 1px solid #9a9a9a; padding: 1px; }
  .photo-card .photo { width: 134px; height: 126px; }
  .photo-card .caption { font-size: 10px; color: var(--red); margin-top: 4px; }
  .photo-card .meta { display: flex; gap: 6px; margin-top: 4px; }

  .tone-hands   { background: linear-gradient(135deg, #7f9a5c, #e4c1a6 50%, #d99a8a); }
  .tone-couple  { background: linear-gradient(135deg, #8a5a3e, #e9c2a8 50%, #f4e7df); }
  .tone-rings   { background: radial-gradient(circle at 50% 55%, #f0c25a, #a98040 45%, #ece4da 85%); }
  .tone-portrait{ background: linear-gradient(135deg, #6b4a32, #d9a588 55%, #efe3d4); }
  .tone-garden  { background: linear-gradient(90deg, #2f4a22, #8c6d4d 45%, #f0f0ee 60%, #3f5d2a); }
  .tone-veil    { background: linear-gradient(135deg, #c8a89c, #ecd8d0 60%, #d7b8ad); }
  .tone-mono    { background: linear-gradient(135deg, #5f5f5f, #cfcfcf 55%, #8a8a8a); }
  .tone-ceremony{ background: linear-gradient(90deg, #4d6a3a, #2a2a2a 30%, #f4f4f2 50%, #2a2a2a 75%, #6a8a4a); }
  .tone-reach   { background: radial-gradient(circle at 50% 70%, #fffaf0, #e3d2ad 55%, #5b3d22); }
  .tone-ringkiss{ background: linear-gradient(135deg, #3a2b22, #d6a889 50%, #6a8b96); }

  .site-footer .rule-footer { top: 861px; }
  .copyright { position: absolute; left: 223px; top: 874px; font-family: "Arimo", sans-serif; font-size: 9px; color: var(--text); }
  .social { position: absolute; left: 422px; top: 875px; display: flex; gap: 7px; }
  .social span { width: 12px; height: 12px; display: block; }
  .social .s1 { background: #4b67a8; }
  .social .s2 { background: #5bb7e0; }
  .legal { position: absolute; right: 226px; top: 874px; font-family: "Arimo", sans-serif; font-size: 9px; color: var(--text); }
  .legal .sep { margin: 0 6px; }
</style>
</head>
<body>
<svg width="0" height="0" style="position:absolute">
  <defs>
    <symbol id="icon-heart" viewBox="0 0 10 10"><path d="M5 9 L1.2 5.2 A2.2 2.2 0 0 1 5 2.4 A2.2 2.2 0 0 1 8.8 5.2 Z" fill="var(--icon-grey)"/></symbol>
    <symbol id="icon-comment" viewBox="0 0 10 10"><path d="M1 1.5 H9 V6.5 H4.5 L2.5 9 V6.5 H1 Z" fill="var(--gold)"/></symbol>
  </defs>
</svg>

<header class="site-header">
  <div class="rule rule-top"></div>
  <div class="rule rule-bottom"></div>
  <p class="event-date">Saturday 1st July 2013</p>
  <p class="event-venue">St. Aldwyn's Church, Anytown</p>

  <nav class="main-nav">
    <a href="#">Home</a><span class="sep">|</span><a href="#">Albums</a><span class="sep">|</span><a href="#">About</a><span class="sep">|</span><a href="#">Search</a><span class="sep">|</span><a href="#">Login</a>
  </nav>

  <div class="album-actions">
    <span><svg width="13" height="11" viewBox="0 0 13 11"><rect x="0.5" y="0.5" width="12" height="10" fill="none" stroke="var(--gold-dark)"/><rect x="3" y="3" width="7" height="5" fill="var(--gold-dark)"/></svg>Slideshow</span>
    <span><svg width="12" height="12" viewBox="0 0 12 12"><circle cx="9.5" cy="2.5" r="2" fill="var(--gold-dark)"/><circle cx="2.5" cy="6" r="2" fill="var(--gold-dark)"/><circle cx="9.5" cy="9.5" r="2" fill="var(--gold-dark)"/><path d="M9.5 2.5 L2.5 6 L9.5 9.5" stroke="var(--gold-dark)" fill="none"/></svg>Share</span>
    <span><svg width="12" height="13" viewBox="0 0 12 13"><path d="M0.5 0.5 H7 L9 2.5 V12.5 H0.5 Z" fill="none" stroke="var(--gold-dark)"/><path d="M8 8 H12 M10 6 V10" stroke="var(--gold-dark)" stroke-width="1.4"/></svg>Add Photos</span>
  </div>

  <svg class="couple-crest" viewBox="0 0 296 142" aria-hidden="true">
    <ellipse cx="148" cy="71" rx="147" ry="70" fill="var(--gold)"/>
    <ellipse cx="148" cy="70" rx="140" ry="64" fill="#f7d87a"/>
    <ellipse cx="148" cy="70" rx="134" ry="59" fill="var(--white)" stroke="var(--gold-dark)" stroke-width="1"/>
  </svg>
  <div class="couple-names">
    <span class="groom">John Doe</span>
    <span class="weds">weds</span>
    <span class="bride">Alexa</span>
  </div>
</header>

<main class="photo-grid">
  <figure class="photo-card" style="left:222px;top:158px"><div class="frame"><div class="photo tone-hands" role="img" aria-label="Couple's hands with rings over a bouquet"></div></div><figcaption class="caption">Photo name 01</figcaption><div class="meta"><svg width="8" height="8"><use href="#icon-heart"/></svg><svg width="8" height="8"><use href="#icon-comment"/></svg></div></figure>
  <figure class="photo-card" style="left:391px;top:158px"><div class="frame"><div class="photo tone-couple" role="img" aria-label="Bride and groom close together"></div></div><figcaption class="caption">Photo name two</figcaption><div class="meta"><svg width="8" height="8"><use href="#icon-heart"/></svg><svg width="8" height="8"><use href="#icon-comment"/></svg></div></figure>
  <figure class="photo-card" style="left:541px;top:158px"><div class="frame"><div class="photo tone-rings" role="img" aria-label="Two gold wedding rings"></div></div><figcaption class="caption">Photo name III</figcaption><div class="meta"><svg width="8" height="8"><use href="#icon-heart"/></svg><svg width="8" height="8"><use href="#icon-comment"/></svg></div></figure>
  <figure class="photo-card" style="left:691px;top:158px"><div class="frame"><div class="photo tone-portrait" role="img" aria-label="Smiling couple portrait"></div></div><figcaption class="caption">Photo name 4</figcaption><div class="meta"><svg width="8" height="8"><use href="#icon-heart"/></svg><svg width="8" height="8"><use href="#icon-comment"/></svg></div></figure>
  <figure class="photo-card" style="left:841px;top:158px"><div class="frame"><div class="photo tone-garden" role="img" aria-label="Couple embracing in a garden"></div></div><figcaption class="caption">Photo name #005</figcaption><div class="meta"><svg width="8" height="8"><use href="#icon-heart"/></svg><svg width="8" height="8"><use href="#icon-comment"/></svg></div></figure>

  <figure class="photo-card" style="left:222px;top:331px"><div class="frame"><div class="photo tone-ringkiss" role="img" aria-label="Ring held up in front of the couple"></div></div><figcaption class="caption">Photo name 01</figcaption><div class="meta"><svg width="8" height="8"><use href="#icon-heart"/></svg><svg width="8" height="8"><use href="#icon-comment"/></svg></div></figure>
  <figure class="photo-card" style="left:391px;top:331px"><div class="frame"><div class="photo tone-ceremony" role="img" aria-label="Outdoor wedding ceremony"></div></div><figcaption class="caption">Photo name two</figcaption><div class="meta"><svg width="8" height="8"><use href="#icon-heart"/></svg><svg width="8" height="8"><use href="#icon-comment"/></svg></div></figure>
  <figure class="photo-card" style="left:541px;top:331px"><div class="frame"><div class="photo tone-reach" role="img" aria-label="Two hands reaching toward each other"></div></div><figcaption class="caption">Photo name III</figcaption><div class="meta"><svg width="8" height="8"><use href="#icon-heart"/></svg><svg width="8" height="8"><use href="#icon-comment"/></svg></div></figure>
  <figure class="photo-card" style="left:691px;top:331px"><div class="frame"><div class="photo tone-veil" role="img" aria-label="Bride behind a soft veil"></div></div><figcaption class="caption">Photo name 4</figcaption><div class="meta"><svg width="8" height="8"><use href="#icon-heart"/></svg><svg width="8" height="8"><use href="#icon-comment"/></svg></div></figure>
  <figure class="photo-card" style="left:841px;top:331px"><div class="frame"><div class="photo tone-mono" role="img" aria-label="Black and white joined hands with rings"></div></div><figcaption class="caption">Photo name #005</figcaption><div class="meta"><svg width="8" height="8"><use href="#icon-heart"/></svg><svg width="8" height="8"><use href="#icon-comment"/></svg></div></figure>

  <figure class="photo-card" style="left:222px;top:504px"><div class="frame"><div class="photo tone-garden" role="img" aria-label="Couple embracing in a garden"></div></div><figcaption class="caption">Photo name 01</figcaption><div class="meta"><svg width="8" height="8"><use href="#icon-heart"/></svg><svg width="8" height="8"><use href="#icon-comment"/></svg></div></figure>
  <figure class="photo-card" style="left:391px;top:504px"><div class="frame"><div class="photo tone-portrait" role="img" aria-label="Smiling couple portrait"></div></div><figcaption class="caption">Photo name two</figcaption><div class="meta"><svg width="8" height="8"><use href="#icon-heart"/></svg><svg width="8" height="8"><use href="#icon-comment"/></svg></div></figure>
  <figure class="photo-card" style="left:541px;top:504px"><div class="frame"><div class="photo tone-rings" role="img" aria-label="Two gold wedding rings"></div></div><figcaption class="caption">Photo name III</figcaption><div class="meta"><svg width="8" height="8"><use href="#icon-heart"/></svg><svg width="8" height="8"><use href="#icon-comment"/></svg></div></figure>
  <figure class="photo-card" style="left:691px;top:504px"><div class="frame"><div class="photo tone-couple" role="img" aria-label="Bride and groom close together"></div></div><figcaption class="caption">Photo name 4</figcaption><div class="meta"><svg width="8" height="8"><use href="#icon-heart"/></svg><svg width="8" height="8"><use href="#icon-comment"/></svg></div></figure>
  <figure class="photo-card" style="left:841px;top:504px"><div class="frame"><div class="photo tone-hands" role="img" aria-label="Couple's hands with rings over a bouquet"></div></div><figcaption class="caption">Photo name #005</figcaption><div class="meta"><svg width="8" height="8"><use href="#icon-heart"/></svg><svg width="8" height="8"><use href="#icon-comment"/></svg></div></figure>

  <figure class="photo-card" style="left:222px;top:677px"><div class="frame"><div class="photo tone-mono" role="img" aria-label="Black and white joined hands with rings"></div></div><figcaption class="caption">Photo name 01</figcaption><div class="meta"><svg width="8" height="8"><use href="#icon-heart"/></svg><svg width="8" height="8"><use href="#icon-comment"/></svg></div></figure>
  <figure class="photo-card" style="left:391px;top:677px"><div class="frame"><div class="photo tone-veil" role="img" aria-label="Bride behind a soft veil"></div></div><figcaption class="caption">Photo name two</figcaption><div class="meta"><svg width="8" height="8"><use href="#icon-heart"/></svg><svg width="8" height="8"><use href="#icon-comment"/></svg></div></figure>
  <figure class="photo-card" style="left:541px;top:677px"><div class="frame"><div class="photo tone-reach" role="img" aria-label="Two hands reaching toward each other"></div></div><figcaption class="caption">Photo name III</figcaption><div class="meta"><svg width="8" height="8"><use href="#icon-heart"/></svg><svg width="8" height="8"><use href="#icon-comment"/></svg></div></figure>
  <figure class="photo-card" style="left:691px;top:677px"><div class="frame"><div class="photo tone-ceremony" role="img" aria-label="Outdoor wedding ceremony"></div></div><figcaption class="caption">Photo name 4</figcaption><div class="meta"><svg width="8" height="8"><use href="#icon-heart"/></svg><svg width="8" height="8"><use href="#icon-comment"/></svg></div></figure>
  <figure class="photo-card" style="left:841px;top:677px"><div class="frame"><div class="photo tone-ringkiss" role="img" aria-label="Ring held up in front of the couple"></div></div><figcaption class="caption">Photo name #005</figcaption><div class="meta"><svg width="8" height="8"><use href="#icon-heart"/></svg><svg width="8" height="8"><use href="#icon-comment"/></svg></div></figure>
</main>

<footer class="site-footer">
  <div class="rule rule-footer"></div>
  <p class="copyright">Copyright © 2013 www.ouralbumpages.com</p>
  <div class="social"><span class="s1" role="img" aria-label="Social link"></span><span class="s2" role="img" aria-label="Social link"></span></div>
  <p class="legal">All Rights Reserved<span class="sep">|</span>Privacy Policy</p>
</footer>
</body>
</html>
```